依頼詳細
グローバルナビ
左サイドメニュー
横幅:960px

今回は、コンペ用のデザイン作成依頼となります。ロゴや電話番号・その他画像データ等サンプルで作成頂ければ幸いです。

《クライアント様からの要望》
すっきりとした見やすいホームページで、患者様やご家族の方に優しい・温かいイメージをもって欲しい。
ロゴに使用されているカラーコードは、「24569d」となります。基調色として取り入れてください。

総合病院で診療科目が多い為、利用者が情報を探しやすいように工夫してください。
病院のPRポイントとしては、「救急患者の受入れを断らない」地域に最先端医療で貢献する。等

(topページに必要なコンテンツ)
・病院からのお知らせ
・はじめてご来院の方へ
-外来受診のご案内
-診療担当・日時
-休診・代診のお知らせ
-入院のご案内
-セカンドオピニオンについて
・お見舞いの皆様へ
・診療科・施設のご案内
-※別途、診療科・施設については添付ファイルを参照ください。
・当院の紹介
・採用情報
・先進医療センター
・周産期医療センター
・消化器病センター
・乳腺診療センター
・地域医療連携への取り組み
サイトURL
ページ数
1ページ
希望イメージ
シンプル 複雑
単色 カラフル
暗い 明るい
日常 高級
遊び心 厳粛
未来的 伝統的
女性的 男性的
希望する色
ブルーを基調(ロゴカラーコード:24569d)差し色はお任せ
納品ファイル
• フォトショップ形式 (.psd)
• PNG形式 (.png)
補足説明
デザインの作成は、Photoshop・Fireworksのみとなります。Illustratorでの作成は不可とします。
(デザイン参考URL)
http://www.tomebara-kouaikai.gr.jp/
http://www.hinokidai.or.jp/
http://kobu.ntmsu.ac.jp/

現サイトのURLにつきましては、個別にメッセージにてお送りさせて頂きますので、希望される方はメッセージをお送りください。
診療科・その他施設一覧ファイルを追加しました。
既存サイトのURLをお伝えした場合、既存サイトのデザインと同じようなご提案が多いため、期間を延長させて頂きます。
既存サイトのURLはお伝えしませんので、斬新なデザインのご提案をお待ちしております。

全体的にスッキリとしている。病院側の伝えたいポイントをしっかりと捉えている。見やすい等、選定理由となりました。

今回、デザイン作成に応募いただきましてありがとうございます。ご提案いただきました全てのデザインをクライアント様に確認いただき、選定させていただきました。
今後とも、機会がありましたら宜しくお願いいたします。

```html
<!DOCTYPE html>
<html lang="ja">
<head>
<meta charset="utf-8">
<title>翠ヶ丘総合病院</title>
<link href="https://fonts.googleapis.com/css2?family=Noto+Sans+JP:wght@400;500;700&family=Noto+Serif+JP:wght@500;700&display=swap" rel="stylesheet">
<style>
:root{
  --brand:#24569d;
  --brand-dark:#163e78;
  --brand-light:#4f86c6;
  --sky:#e8f1fa;
  --line:#c9d9ec;
  --text:#333;
  --muted:#666;
  --accent:#d9731f;
  --white:#fff;
}
*{box-sizing:border-box;margin:0;padding:0}
html,body{width:819px;height:1200px;overflow:hidden}
body{font-family:"Noto Sans JP",sans-serif;color:var(--text);background:var(--white);font-size:11px;position:relative}
a{color:inherit;text-decoration:none}

.site-header{position:absolute;left:0;top:0;width:819px;height:74px}
.brand{position:absolute;left:22px;top:14px;display:flex;align-items:center;gap:8px}
.brand-mark{width:30px;height:30px;background:var(--brand);border-radius:50%}
.brand-name{color:var(--brand);font-weight:700;line-height:1.15}
.brand-name small{display:block;font-size:10px}
.brand-name span{font-size:20px;letter-spacing:.08em}
.utility{position:absolute;right:22px;top:0;display:flex;gap:2px}
.utility a{background:var(--brand);color:var(--white);font-size:9px;padding:3px 10px;border-radius:0 0 3px 3px}
.utility a.lang{background:var(--white);color:var(--brand);border:1px solid var(--line);border-top:0}

.global-nav{position:absolute;left:0;top:74px;width:819px;height:41px;display:flex;background:linear-gradient(#3a70b8,var(--brand));border-bottom:2px solid var(--brand-dark)}
.global-nav a{flex:1;color:var(--white);font-size:13px;font-weight:500;display:flex;align-items:center;justify-content:center;border-right:1px solid rgba(255,255,255,.3)}
.global-nav a.current{background:var(--brand-dark)}

.hero{position:absolute;left:0;top:115px;width:819px;height:295px}
.hero-photo{position:absolute;inset:0;background:linear-gradient(90deg,#f3f7fb 0%,#dfeaf5 40%,#c7dcef 75%,#9fc0e0 100%)}
.hero-copy{position:absolute;left:300px;top:36px;font-family:"Noto Serif JP",serif;color:var(--brand-dark);font-size:21px;font-weight:700;line-height:1.6;letter-spacing:.04em}
.hero-links{position:absolute;left:225px;top:160px;display:flex;gap:6px}
.circle-link{width:112px;height:112px;border-radius:50%;background:rgba(255,255,255,.92);border:3px solid var(--brand-light);display:flex;flex-direction:column;align-items:center;justify-content:center;color:var(--brand);font-size:17px;font-weight:700;line-height:1.25;text-align:center}
.circle-link svg{margin-top:6px}
.slider-dots{position:absolute;left:0;top:410px;width:819px;height:22px;display:flex;justify-content:center;align-items:center;gap:6px;background:var(--sky)}
.slider-dots i{width:8px;height:8px;border-radius:50%;background:var(--line)}
.slider-dots i.on{background:var(--brand)}

.sidebar{position:absolute;left:22px;top:442px;width:224px}
.hours{border:1px solid var(--line);background:var(--white)}
.hours h2{background:var(--brand);color:var(--white);font-size:13px;padding:7px 10px}
.hours-body{padding:8px 10px;background:linear-gradient(var(--sky),var(--white))}
.hours dt{color:var(--accent);font-weight:700;font-size:11px;margin-top:6px}
.hours dd{font-size:10px;line-height:1.6;color:var(--text)}
.hours .note{font-size:9px;color:var(--muted);line-height:1.5;margin-top:6px}
.center-links{margin-top:12px;display:flex;flex-direction:column;gap:8px}
.center-links a{height:40px;background:linear-gradient(#3c72ba,var(--brand-dark));color:var(--white);font-size:13px;font-weight:500;display:flex;align-items:center;justify-content:center;border-radius:3px}
.privacy{display:block;margin-top:16px;font-size:10px;color:var(--brand)}
.privacy::before{content:"▶ ";font-size:7px}

.main{position:absolute;left:268px;top:442px;width:529px}
.section-title{display:flex;align-items:center;gap:6px;color:var(--brand);font-size:13px;font-weight:700;border-bottom:2px solid var(--brand);padding-bottom:4px}
.section-title::before{content:"";width:12px;height:12px;background:var(--brand);border-radius:2px}
.dept-links{display:flex;gap:8px;margin-top:10px}
.dept-links a{flex:1;height:32px;background:linear-gradient(#fff,#e3edf8);border:1px solid var(--line);display:flex;align-items:center;justify-content:center;color:var(--brand);font-weight:700;font-size:12px}
.news{margin-top:24px}
.news-list{list-style:none;margin-top:6px}
.news-list li{padding:6px 2px;border-bottom:1px dotted var(--line);font-size:10px;line-height:1.5}
.news-list time{display:block;color:var(--muted);font-size:9px}
.news-list a{color:var(--brand)}
.news-more{display:block;text-align:right;font-size:9px;color:var(--brand);margin-top:6px}
.feature-cards{display:flex;gap:10px;margin-top:16px}
.card{flex:1}
.card-photo{height:96px;border:1px solid var(--line)}
.card-photo.a{background:linear-gradient(135deg,#e9eef3,#c7d3df)}
.card-photo.b{background:linear-gradient(135deg,#dce9f5,#a9c4e0)}
.card-photo.c{background:linear-gradient(135deg,#dfe5ea,#9fb0c0)}
.card-label{display:block;font-size:10px;color:var(--brand);margin-top:4px}
.card-label::before{content:"▶ ";font-size:7px}

.pagetop{position:absolute;right:22px;top:1003px;background:var(--brand);color:var(--white);font-size:10px;padding:4px 12px;border-radius:4px 4px 0 0}
.site-footer{position:absolute;left:0;top:1024px;width:819px;height:176px;background:var(--brand)}
.footer-inner{padding:14px 22px;color:var(--white)}
.footer-inner h3{font-size:11px;font-weight:700;margin-bottom:8px}
.related{display:flex;flex-wrap:wrap;gap:6px 22px;font-size:10px}
.related a::before{content:"■ ";font-size:7px}
.copyright{position:absolute;left:0;bottom:0;width:819px;height:34px;background:var(--brand-dark);color:var(--white);font-size:9px;display:flex;align-items:center;justify-content:flex-end;padding-right:22px}
</style>
</head>
<body>
<header class="site-header">
  <div class="brand">
    <span class="brand-mark"></span>
    <div class="brand-name"><small>医療法人 青葉会</small><span>翠ヶ丘総合病院</span></div>
  </div>
  <nav class="utility">
    <a href="#">ホーム</a><a href="#">サイトマップ</a><a href="#">お問い合わせ</a><a href="#" class="lang">English</a>
  </nav>
</header>

<nav class="global-nav">
  <a href="#" class="current">翠ヶ丘総合病院について</a>
  <a href="#">診療科のご案内</a>
  <a href="#">受診される皆様へ</a>
  <a href="#">ご面会について</a>
  <a href="#">交通アクセス</a>
</nav>

<section class="hero">
  <div class="hero-photo" role="img" aria-label="笑顔の家族と病院の建物、青空の写真"></div>
  <p class="hero-copy">救急患者の受入れ、最先端医療の実施で、<br>地域の皆様の笑顔を守ります。</p>
  <div class="hero-links">
    <a href="#" class="circle-link">初めて<br>ご来院の方へ
      <svg width="16" height="16" viewBox="0 0 16 16"><circle cx="8" cy="8" r="8" fill="#24569d"/><path d="M6 4l4 4-4 4" stroke="#fff" stroke-width="2" fill="none"/></svg></a>
    <a href="#" class="circle-link">お見舞いの<br>皆様へ
      <svg width="16" height="16" viewBox="0 0 16 16"><circle cx="8" cy="8" r="8" fill="#24569d"/><path d="M6 4l4 4-4 4" stroke="#fff" stroke-width="2" fill="none"/></svg></a>
  </div>
</section>
<div class="slider-dots"><i class="on"></i><i></i><i></i></div>

<aside class="sidebar">
  <section class="hours">
    <h2>診療・受付時間</h2>
    <div class="hours-body">
      <dl>
        <dt>診療時間</dt>
        <dd>平日 9:00〜11:30 ／ 14:00〜17:00</dd>
        <dd>土曜 9:00〜11:30</dd>
        <dt>受付時間</dt>
        <dd>初診 8:30〜11:00 ／ 13:30〜16:00</dd>
        <dd>再診 8:00〜11:30 ／ 13:30〜16:30</dd>
        <dt>休診日</dt>
        <dd>日曜・祝日・年末年始</dd>
      </dl>
      <p class="note">救急の方は24時間受け付けております。診療科により受付時間が異なる場合がありますので、各診療科の案内をご確認ください。</p>
    </div>
  </section>
  <nav class="center-links">
    <a href="#">先進医療センター</a>
    <a href="#">周産期医療センター</a>
    <a href="#">消化器病センター</a>
    <a href="#">乳腺診療センター</a>
  </nav>
  <a href="#" class="privacy">個人情報保護方針</a>
</aside>

<main class="main">
  <section>
    <h2 class="section-title">診療科・施設のご案内</h2>
    <div class="dept-links">
      <a href="#">内科</a><a href="#">外科</a><a href="#">放射線科</a><a href="#">治療・検査設備</a>
    </div>
  </section>
  <section class="news">
    <h2 class="section-title">病院からのお知らせ</h2>
    <ul class="news-list">
      <li><time>2011.10.05</time><a href="#">外来診療担当表を更新しました</a></li>
      <li><time>2011.09.28</time>地域医療連携センターより<a href="#">連携医療機関向け勉強会のご案内</a>を掲載しました</li>
      <li><time>2011.09.20</time><a href="#">休診・代診のお知らせ</a>を更新しました</li>
      <li><time>2011.09.12</time><a href="#">採用情報</a>に看護師募集のご案内を追加しました</li>
      <li><time>2011.09.01</time>院内にて<a href="#">健康講座</a>を開催します</li>
      <li><time>2011.08.22</time><a href="#">乳腺診療センター</a>のページを更新しました</li>
    </ul>
    <a href="#" class="news-more">お知らせ一覧へ</a>
  </section>
  <div class="feature-cards">
    <a href="#" class="card"><div class="card-photo a" role="img" aria-label="病院外観の写真"></div><span class="card-label">当院の紹介</span></a>
    <a href="#" class="card"><div class="card-photo b" role="img" aria-label="医療スタッフの写真"></div><span class="card-label">採用情報</span></a>
    <a href="#" class="card"><div class="card-photo c" role="img" aria-label="地域の街並みの写真"></div><span class="card-label">地域医療連携への取り組み</span></a>
  </div>
</main>

<a href="#" class="pagetop">ページトップへ</a>
<footer class="site-footer">
  <div class="footer-inner">
    <h3>関連病院・施設</h3>
    <div class="related">
      <a href="#">青葉記念病院</a><a href="#">緑風台病院</a><a href="#">青葉中央病院</a><a href="#">ひだまりホーム</a><a href="#">青葉看護専門学校</a>
    </div>
  </div>
  <p class="copyright">Copyright © Aobakai Association All Rights Reserved.</p>
</footer>
</body>
</html>
```